Design a Website Mockup for Bright Pebble's Learning Center (Daycare)

A local, brand new, learning center, or daycare, needs a website mockup for a homepage and general content page. I have also included the daycare's logos that need to be integrated into the design (see attached images). The overall color scheme needs to blend well with the logos. I am expecting two mockups, one for the homepage and one for the general content pages in psd layered format. Any assets, including images and fonts need to be provided along with the final mockups.

```html
<!DOCTYPE html>
<html lang="en">
<head>
<meta charset="utf-8">
<title>Bright Pebble's Learning Center</title>
<link href="https://fonts.googleapis.com/css2?family=Ubuntu:wght@400;500;700&family=Open+Sans:wght@400;600&display=swap" rel="stylesheet">
<style>
:root{
  --orange:#f7941d;
  --red:#c41e32;
  --red-dark:#b01a2c;
  --green:#0aa64b;
  --blue:#2578c8;
  --sky:#b4e8e9;
  --teal:#43b5b9;
  --white:#ffffff;
  --text-dark:#444;
  --line:#c9a4a4;
}
*{margin:0;padding:0;box-sizing:border-box}
html,body{width:1200px;height:2179px;overflow:hidden}
body{font-family:"Open Sans",sans-serif;background:var(--sky);color:var(--white)}
.page{position:relative;width:1200px;height:2179px;overflow:hidden;
  background:linear-gradient(180deg,#2fa9ae 0,#6ccacc 120px,#a6e2e3 290px,var(--sky) 420px,var(--sky) 100%)}
.abs{position:absolute}

/* header */
.social{left:89px;top:96px;display:flex;gap:7px}
.social span{width:37px;height:37px;border-radius:50%;display:block}
.brand{left:440px;top:40px;width:320px;text-align:center;font-family:"Ubuntu",sans-serif;font-weight:700;font-size:28px;line-height:36px;color:var(--red)}
.brand .dot{display:block;width:60px;height:60px;border-radius:50%;background:var(--orange);margin:0 auto 14px}
.login{left:995px;top:97px;width:114px;height:40px;background:var(--red);font-size:14px;display:flex;align-items:center;justify-content:center}

/* nav */
.nav{left:88px;top:228px;width:1023px;height:55px;background:var(--red);display:flex;font-size:14px}
.nav a{color:var(--white);text-decoration:none;display:flex;align-items:center;padding:0 24px}
.nav a.active{background:var(--orange);width:91px;justify-content:center;padding:0}
.nav .search{margin-left:auto;width:258px;background:var(--red-dark);display:flex;align-items:center;justify-content:space-between;padding:0 22px;color:#f1c8cd;font-size:13px}

/* slider */
.slider{left:88px;top:307px;width:1023px;height:421px;background:linear-gradient(135deg,#6b4c3b,#a58a70 45%,#8a5a4a 70%,#5d6b3e)}
.slider-copy{left:88px;top:420px;width:1023px;text-align:center}
.slider-copy h1{font-family:"Ubuntu",sans-serif;font-weight:700;font-size:43px;text-shadow:0 2px 4px rgba(0,0,0,.4)}
.slider-copy .bar{width:66px;height:4px;background:var(--orange);margin:14px auto 16px}
.slider-copy p{font-size:13px;line-height:26px;width:760px;margin:0 auto;text-shadow:0 1px 2px rgba(0,0,0,.5)}
.dots{left:566px;top:672px;display:flex;gap:9px}
.dots span{width:16px;height:16px;border-radius:50%}
.arrow{width:67px;height:67px;border-radius:50%;top:482px;display:flex;align-items:center;justify-content:center}

/* tiles */
.tile{top:804px;width:240px;height:183px;display:flex;flex-direction:column;align-items:center;justify-content:flex-end;padding-bottom:16px;font-family:"Ubuntu",sans-serif;font-size:18px}
.tile svg{margin-bottom:18px}

/* welcome */
.welcome{left:88px;top:1029px;width:763px;height:340px;background:linear-gradient(135deg,#2e7fcc,#3a8ad2 60%,#2f7bc4);padding:32px 36px}
.welcome h2{font-family:"Ubuntu",sans-serif;font-weight:500;font-size:28px;color:var(--orange)}
.welcome .lead{font-size:17px;margin:10px 0 18px}
.welcome p{font-size:12.5px;line-height:18px;margin-bottom:16px}
.btn{display:inline-flex;align-items:center;justify-content:center;background:var(--orange);color:var(--white);font-size:13px}
.welcome .btn{width:150px;height:46px;margin-top:12px}
.posts{left:869px;top:1029px;width:240px;height:340px;background:var(--red)}
.posts h3{background:var(--orange);height:44px;line-height:44px;padding-left:25px;font-weight:400;font-size:15px}
.posts ul{list-style:none;padding:18px 24px 0 24px}
.posts li{font-size:11px;line-height:18px;padding-bottom:10px;margin-bottom:12px;border-bottom:1px solid rgba(255,255,255,.3)}
.posts li:last-child{border:none}
.posts .date{color:var(--orange);font-size:10px;display:block}

/* featured */
.featured-title{left:88px;top:1446px;font-family:"Ubuntu",sans-serif;font-size:18px;color:var(--red)}
.featured-line{left:254px;top:1459px;width:763px;height:1px;background:var(--line)}
.fbtn{top:1443px;width:33px;height:33px;display:flex;align-items:center;justify-content:center}
.card{top:1507px;width:240px;height:181px}
.card-english{background:var(--orange);display:flex;flex-direction:column;align-items:center;justify-content:center;font-family:"Ubuntu",sans-serif;font-size:19px}
.card-english .btn{background:var(--blue);width:120px;height:37px;margin-top:14px;font-family:"Open Sans",sans-serif;font-size:12px}

/* footer */
.footer{left:0;top:1773px;width:1200px;height:347px;background:linear-gradient(90deg,#c92a3c,#c9344a 50%,#c12638)}
.fcol{top:1818px;width:220px}
.fcol h4{font-family:"Ubuntu",sans-serif;font-weight:400;font-size:16px;margin-bottom:22px}
.fcol ul{list-style:none}
.fcol li{font-size:12.5px;height:39px;line-height:16px;border-bottom:1px solid rgba(255,255,255,.15);margin-bottom:0;padding-top:6px}
.course{display:flex;gap:16px;margin-bottom:26px}
.course .thumb{width:70px;height:64px;flex:none;background:linear-gradient(135deg,#e9c8a8,#c98e6e)}
.course b{font-weight:400;font-size:13px;display:block;margin:2px 0 8px}
.course span{font-size:11.5px;line-height:15px;display:block}
.contact p{font-size:11.5px;line-height:17.5px;margin-bottom:18px}
.bottom{left:0;top:2120px;width:1200px;height:59px;background:var(--orange);font-size:12px;padding:26px 88px}
</style>
</head>
<body>
<div class="page">

  <div class="abs social" aria-label="Social links">
    <span style="background:#d31f2b"></span>
    <span style="background:#f6b414"></span>
    <span style="background:#2578c8"></span>
    <span style="background:#f7941d"></span>
  </div>
  <div class="abs brand"><span class="dot"></span>Bright Pebble's<br>Learning Center</div>
  <div class="abs login">Login</div>

  <nav class="abs nav">
    <a class="active" href="#">Home</a>
    <a href="#">Courses</a>
    <a href="#">Documentation</a>
    <a href="#">Typography</a>
    <a href="#">Blog</a>
    <a href="#">Contact Us</a>
    <div class="search">Search...
      <svg width="18" height="18" viewBox="0 0 18 18"><circle cx="7.5" cy="7.5" r="5.5" fill="none" stroke="#fff" stroke-width="2"/><path d="M11.5 11.5l5 5" stroke="#fff" stroke-width="2"/></svg>
    </div>
  </nav>

  <div class="abs slider" role="img" aria-label="Photo of children sitting at desks in a classroom"></div>
  <div class="abs slider-copy">
    <h1>Happy Learning Center</h1>
    <div class="bar"></div>
    <p>Lorem ipsum dolor sit amet, consectetuer adipiscing elit. Aenean commodo ligula eget dolor. Aenean massa. Cum sociis natoque penatibus et magnis dis parturient montes, nascetur ridiculus mus. Donec quam felis..</p>
  </div>
  <div class="abs dots"><span style="background:var(--orange)"></span><span style="background:var(--red)"></span><span style="background:var(--green)"></span></div>
  <div class="abs arrow" style="left:56px;background:var(--orange)"><svg width="16" height="26" viewBox="0 0 16 26"><path d="M13 2L3 13l10 11" fill="none" stroke="#fff" stroke-width="2"/></svg></div>
  <div class="abs arrow" style="left:1077px;background:var(--blue)"><svg width="16" height="26" viewBox="0 0 16 26"><path d="M3 2l10 11L3 24" fill="none" stroke="#fff" stroke-width="2"/></svg></div>

  <div class="abs tile" style="left:88px;background:var(--orange)">
    <svg width="84" height="80" viewBox="0 0 84 80"><path d="M6 36l30-4 22-28c4-4 10-2 8 4L52 34l28 4v6l-28 4 14 26c2 6-4 8-8 4L36 50 6 46z" fill="#fff"/></svg>Love
  </div>
  <div class="abs tile" style="left:349px;background:var(--red)">
    <svg width="86" height="80" viewBox="0 0 86 80"><circle cx="43" cy="14" r="12" fill="#fff"/><path d="M4 36l39 10 39-10v36L43 80 4 72z" fill="#fff"/><path d="M43 46v34" stroke="#c41e32" stroke-width="3"/></svg>Learn
  </div>
  <div class="abs tile" style="left:611px;background:var(--green)">
    <svg width="76" height="76" viewBox="0 0 76 76"><path d="M40 8H8v60h60V36" fill="none" stroke="#fff" stroke-width="6"/><path d="M60 4l12 12-32 32H28V36z" fill="#fff"/></svg>Write
  </div>
  <div class="abs tile" style="left:869px;background:var(--blue)">
    <svg width="98" height="80" viewBox="0 0 98 80"><path d="M20 56a14 14 0 010-28 20 20 0 0138-8 16 16 0 0126 10 13 13 0 01-2 26z" fill="#fff"/><circle cx="40" cy="66" r="5" fill="#fff"/><circle cx="30" cy="76" r="3" fill="#fff"/></svg>Dream
  </div>

  <section class="abs welcome">
    <h2>Welcome to Bright Pebble's Learning Center !</h2>
    <div class="lead">Lorem ipsum dolor sit amet, consectetuer adipiscing elit.</div>
    <p>Lorem ipsum dolor sit amet, consectetuer adipiscing elit. Aenean commodo ligula eget dolor. Aenean massa. Cum sociis natoque penatibus et magnis dis parturient montes, nascetur ridiculus mus.</p>
    <p>Lorem ipsum dolor sit amet, consectetuer adipiscing elit. Aenean commodo ligula eget dolor. Aenean massa. Cum sociis natoque penatibus et magnis dis parturient montes, nascetur ridiculus mus. Donec quam felis, ultricies nec, pellentesque eu, pretium quis, sem. Nulla consequat massa quis enim. Donec pede justo, fringilla vel, aliquet nec, vulputate eget, arcu. In enim justo, rhoncus ut, imperdiet a, venenatis vitae, justo. Nullam dictum .</p>
    <a class="btn">Read More</a>
  </section>

  <aside class="abs posts">
    <h3>Recent Posts</h3>
    <ul>
      <li>New Arts and Crafts Class Added to Our Activities<span class="date">JUNE 6, 2014</span></li>
      <li>Here Are the Holidays for the Month of June<span class="date">JUNE 6, 2014</span></li>
      <li>How to Use Video Games as a Learning Tool<span class="date">JUNE 6, 2014</span></li>
    </ul>
  </aside>

  <div class="abs featured-title">Featured Courses</div>
  <div class="abs featured-line"></div>
  <div class="abs fbtn" style="left:1040px;background:var(--red)"><svg width="10" height="14" viewBox="0 0 10 14"><path d="M8 1L2 7l6 6" fill="none" stroke="#fff" stroke-width="2"/></svg></div>
  <div class="abs fbtn" style="left:1076px;background:var(--green)"><svg width="10" height="14" viewBox="0 0 10 14"><path d="M2 1l6 6-6 6" fill="none" stroke="#fff" stroke-width="2"/></svg></div>

  <div class="abs card" style="left:88px;background:linear-gradient(135deg,#e8e2d6,#d9c49a 55%,#e6b940)" role="img" aria-label="Photo of a girl reading a book"></div>
  <div class="abs card card-english" style="left:349px">English<a class="btn">Read More</a></div>
  <div class="abs card" style="left:611px;background:linear-gradient(135deg,#c9a27a,#5a7fa8 55%,#e8e2d8)" role="img" aria-label="Photo of a teacher helping a child draw"></div>
  <div class="abs card" style="left:869px;background:linear-gradient(135deg,#c9c0a8,#a7b7c3 50%,#cf7b5a)" role="img" aria-label="Photo of children looking at a laptop"></div>

  <footer class="abs footer"></footer>
  <div class="abs fcol" style="left:88px">
    <h4>About University</h4>
    <ul><li>History &amp; Mission</li><li>Employment</li><li>Social Media</li><li>Community</li><li>Management</li><li style="border:none">Employment</li></ul>
  </div>
  <div class="abs fcol" style="left:344px">
    <h4>Categories</h4>
    <ul><li>Activities</li><li>Announcements</li><li>Education</li><li>Feedback</li><li style="border:none">Programs</li></ul>
  </div>
  <div class="abs fcol" style="left:597px;width:250px">
    <h4>Popular Cources</h4>
    <div class="course"><div class="thumb" role="img" aria-label="Photo of a smiling child"></div><div><b>Starting a Startup</b><span>Lorem ipsum dolor sit amet, consectetuer .</span></div></div>
    <div class="course"><div class="thumb" role="img" aria-label="Photo of a child with a book"></div><div><b>Starting a Startup</b><span>Lorem ipsum dolor sit amet, consectetuer .</span></div></div>
  </div>
  <div class="abs fcol contact" style="left:853px;width:240px">
    <h4>Contact Us</h4>
    <p>48 Maple Grove Road<br>Willow Creek District Springfield<br>United States , 40213</p>
    <p>Phone : +1 555 210 4412<br>Fax: +1 555 210 4413<br>Email: hello@brightpebble.org<br>Webiste: www.brightpebble.org</p>
  </div>

  <div class="abs bottom">Copyright@2015 | All Right Reserved</div>
</div>
</body>
</html>
```